Sunbird Therapy Services needs upgraded website

Upgrade current website www.sunbirdtherapy.com.au. Need to incorporate new logo (attached). Family friendly and professional feel. Use of colour green. We are based in Melbourne, Australia and work with children aged 0-16 who have additional needs requiring therapy.

Target Market(s)

Parents of children with special needs.

Colors
000000

Requirements
Must have
• The current content/ pictures are already on the website and can be replicated, just with a fresh look. Additionally need an FAQ section. Must incorporate logo and have consistency on each page. Needs to be accessible on tablets/devices (current website only shows home page on devices, however actual sites has many sub pages (approx. 7). I will need to be able to easily edit the content down the track and potentially add pages.

```html
<!DOCTYPE html>
<html lang="en">
<head>
<meta charset="utf-8">
<title>Sunbird Therapy Services</title>
<link href="https://fonts.googleapis.com/css2?family=Lato:wght@400;700&display=swap" rel="stylesheet">
<style>
:root{
  --green:#3bb54a;
  --green-dark:#1f7a32;
  --green-deep:#0f5a24;
  --black:#000;
  --ink:#222;
  --white:#fff;
  --footer-bar:#1d1d1d;
}
*{box-sizing:border-box;margin:0;padding:0}
html,body{width:794px;height:1200px;overflow:hidden}
body{position:relative;font-family:'Lato',sans-serif;background:var(--white);color:var(--ink)}
.header{position:absolute;left:0;top:0;width:794px;height:64px;background:var(--green)}
.brand{position:absolute;left:44px;top:18px;display:flex;align-items:center;gap:8px;color:var(--green-deep);font-size:22px;font-weight:700}
.brand-mark{width:22px;height:22px;background:var(--green-deep)}
.top-links{position:absolute;right:58px;top:0;display:flex;font-size:9px;color:var(--white)}
.top-links a{padding:7px 10px;color:var(--white);text-decoration:none}
.top-links a.active{background:var(--green-dark)}
.nav{position:absolute;left:40px;top:64px;width:714px;height:31px;background:var(--black);display:flex;align-items:center;padding-left:12px;font-size:9.5px;color:var(--white)}
.nav span{margin-right:22px}
.nav svg{margin-right:16px}
.hero{position:absolute;left:0;top:95px;width:794px;height:289px;background:linear-gradient(180deg,#4f9fd8 0%,#a9d2ee 38%,#c7c9c2 48%,#1d6f86 70%,#155c70 100%)}
.hero-title{position:absolute;left:228px;top:114px;width:328px;height:34px;background:rgba(40,40,40,.75);color:var(--white);font-size:19px;text-align:center;line-height:34px}
.hero-arrows{position:absolute;left:379px;top:244px;width:37px;height:30px;background:rgba(40,40,40,.75)}
.welcome h1{position:absolute;left:52px;top:402px;font-size:15px;font-weight:400;color:var(--green-deep);letter-spacing:.3px}
.welcome-text{position:absolute;left:54px;top:431px;width:460px;font-size:8.6px;line-height:11px;color:var(--ink)}
.welcome-text p{margin-bottom:10px}
.welcome-text a{color:var(--green)}
.welcome-photo{position:absolute;left:532px;top:403px;width:207px;height:154px;border:1px solid #ddd;padding:6px;background:var(--white)}
.welcome-photo div{width:100%;height:100%;background:linear-gradient(180deg,#fff 0%,#e8eef3 60%,#fff 100%)}
.services{position:absolute;left:0;top:588px;width:794px;height:205px;background:var(--green);display:flex}
.service{position:relative;text-align:center;color:var(--white);padding-top:16px}
.service:nth-child(2){background:linear-gradient(180deg,#3bb54a,#34a844)}
.service h2{font-size:14px;font-weight:400;margin-bottom:6px}
.service hr{width:80px;margin:0 auto 10px;border:0;border-top:1px solid var(--white)}
.service p{font-size:8px;line-height:11px;width:180px;margin:0 auto}
.service .date{font-size:11px;margin-top:10px}
.btn{position:absolute;bottom:47px;left:50%;transform:translateX(-50%);background:#111;color:var(--white);font-size:9px;padding:7px 11px;white-space:nowrap}
.staff{position:absolute;left:0;top:793px;width:794px;height:209px;background:var(--black);color:var(--white)}
.staff h2{position:absolute;left:0;width:794px;top:24px;text-align:center;font-size:14px;font-weight:400}
.staff hr{position:absolute;left:362px;top:48px;width:70px;border:0;border-top:1px solid var(--white)}
.staff-photo{position:absolute;left:102px;top:58px;width:114px;height:114px;border-radius:50%;background:radial-gradient(circle at 45% 40%,#c59a86,#6d4a3c 70%,#3a2a22)}
.staff-name{position:absolute;left:228px;top:63px;font-size:14px;color:var(--green)}
.staff-role{position:absolute;left:228px;top:86px;font-size:8.5px;color:var(--green)}
.staff-bio{position:absolute;left:229px;top:102px;width:478px;font-size:7.6px;line-height:11px}
.staff-more{position:absolute;left:229px;top:167px;font-size:8px;color:var(--green)}
.footer{position:absolute;left:0;top:1002px;width:794px;height:167px;background:var(--green);color:var(--white)}
.footer h3{position:absolute;top:26px;font-size:13.5px;font-weight:700;letter-spacing:.3px}
.quick{position:absolute;left:75px;top:56px;list-style:none;font-size:8.5px;font-weight:700;line-height:14.7px}
.contact-row{position:absolute;left:238px;display:flex;gap:9px;font-size:7.8px;line-height:10px}
.news-text{position:absolute;left:442px;top:54px;width:125px;font-size:8.3px;line-height:15px}
.email{position:absolute;left:442px;top:86px;width:121px;height:22px;background:var(--white);color:#777;font-size:8.5px;line-height:22px;padding-left:18px}
.subscribe{position:absolute;left:442px;top:116px;width:121px;height:21px;background:#111;font-size:8.5px;line-height:21px;text-align:center}
.socials{position:absolute;left:612px;top:58px;display:flex;gap:6px}
.socials span{width:19px;height:19px;border-radius:50%}
.bottom-bar{position:absolute;left:0;top:1169px;width:794px;height:31px;background:var(--footer-bar);color:var(--white);text-align:center;font-size:8px;line-height:31px}
</style>
</head>
<body>
<header class="header">
  <div class="brand"><span class="brand-mark"></span>Sunbird Therapy Services</div>
  <nav class="top-links"><a class="active">Job Opportunities</a><a>Links</a><a>Contact Us</a></nav>
</header>
<nav class="nav">
  <svg width="9" height="9" viewBox="0 0 10 10"><path d="M5 0L0 5h1.5v5h2.5V7h2v3h2.5V5H10z" fill="#fff"/></svg>
  <span>Occupational Therapy</span><span>Therapy Services</span><span>Group Sessions</span><span>Training Packages</span><span>Meet The Staff</span><span>Fees / Funding Options</span><span>Parent Resources</span>
</nav>
<section class="hero" role="img" aria-label="Photograph of a harbour city skyline on a sunny day">
  <div class="hero-title">Sunbird Therapy Services</div>
  <div class="hero-arrows"><svg width="37" height="30" viewBox="0 0 37 30"><path d="M15 8l-6 7 6 7M22 8l6 7-6 7" stroke="#fff" fill="none" stroke-width="1.2"/></svg></div>
</section>
<section class="welcome">
  <h1>WELCOME TO OUR WEB SITE!</h1>
  <div class="welcome-text">
    <p>Sunbird Therapy Services is a specialist Occupational Therapy (O.T) provider for children (aged 0-16). Based in Fernvale, Victoria, Sunbird provides comprehensive, private therapy services to children with a broad range of difficulties and disabilities.</p>
    <p>With a special focus on early intervention, Sunbird strongly believes in goal based, child and family centered therapy, ideally located in the child's natural environment. For this reason we specialise in home, kindergarten and school based intervention.</p>
    <p>Sunbird's client base spans across many areas of Melbourne. <a>Click here to view our catchment zone for home/kindergarten/school based therapy services.</a> For families living out of our catchment zone we have a clinic located in Fernvale. Sunbird therapy is part of the national provider panel for both the Better Start Initiative (BSI) and Helping Children With Austism (HCWA).</p>
  </div>
  <div class="welcome-photo"><div role="img" aria-label="Photograph of happy children jumping in the air"></div></div>
</section>
<section class="services">
  <div class="service" style="width:277px">
    <h2>Occupational Therapy</h2><hr>
    <p>An occupational therapist (O.T) sounds like someone you see for help with a job. Well I guess this is true... Children have very important jobs- to play, make friends, be successful at home tasks such as dressing and feeding, and probably most importantly, to reach their social and academic potential.</p>
    <span class="btn">Read More</span>
  </div>
  <div class="service" style="width:247px">
    <h2>Therapy Services</h2><hr>
    <p>Assessments are generally conducted at your home or school/kindergarten. A range of standardised and non-standardised assessments are used at Sunbird. A thorough assessment is always conducted before therapy can commence.</p>
    <span class="btn">Read More</span>
  </div>
  <div class="service" style="width:270px">
    <h2>Group Sessions</h2><hr>
    <p>Unfortunetly there are no group services being run at the moment, however check in regularly as this is likely to change!</p>
    <p class="date">July 2011</p>
    <span class="btn">Read More</span>
  </div>
</section>
<section class="staff">
  <h2>Meet the Staff</h2><hr>
  <svg style="position:absolute;left:54px;top:96px" width="12" height="24" viewBox="0 0 12 24"><path d="M11 1L1 12l10 11" stroke="#fff" fill="none" stroke-width="1.2"/></svg>
  <svg style="position:absolute;left:727px;top:96px" width="12" height="24" viewBox="0 0 12 24"><path d="M1 1l10 11L1 23" stroke="#fff" fill="none" stroke-width="1.2"/></svg>
  <div class="staff-photo" role="img" aria-label="Portrait photograph of the director with two young children"></div>
  <div class="staff-name">Clara Whitfield</div>
  <div class="staff-role">Director / Occupational Therapist</div>
  <p class="staff-bio">Graduating in 2000, Clara has worked as a Paediatric Occupational Therapist in the major children's hospitals in Melbourne, Sydney and London. During this time she has been lucky enough to work beside leading neurodevelopmental medical consultants, and is now able to bring a range of approaches to her work with children. She has specialist experience assessing and working with children with developmental coordination disorder (DCD)/ dyspraxia, cerebral palsy, acquired brain injury/ brain tumors and children with global developmental delay.</p>
  <span class="staff-more">ReadMore ...</span>
</section>
<footer class="footer">
  <h3 style="left:72px">QUICK LINKS</h3>
  <ul class="quick"><li>Home</li><li>About Us</li><li>Services</li><li>Testimonials</li><li>Career</li><li>Contact Us</li></ul>
  <h3 style="left:237px">CONTACT INFO</h3>
  <div class="contact-row" style="top:56px"><svg width="10" height="10" viewBox="0 0 10 10"><path d="M5 0L0 5h1.5v5h2.5V7h2v3h2.5V5H10z" fill="#fff"/></svg><span>Sunbird Therapy Services<br>P.O.Box 512 Fernvale VIC 3190</span></div>
  <div class="contact-row" style="top:89px"><svg width="10" height="10" viewBox="0 0 10 10"><rect x="2.5" y="0.5" width="5" height="9" rx="1" stroke="#fff" fill="none"/></svg><span>Phone: (03) 9000 1234</span></div>
  <div class="contact-row" style="top:111px"><svg width="10" height="10" viewBox="0 0 10 10"><rect x="0.5" y="2" width="9" height="6" stroke="#fff" fill="none"/><path d="M0.5 2l4.5 3.5L9.5 2" stroke="#fff" fill="none"/></svg><span>Email: admin@sunbirdtherapy.com.au</span></div>
  <h3 style="left:440px">NEWSLETTER</h3>
  <p class="news-text">Sign up to receive the latest updates</p>
  <div class="email">Email id</div>
  <div class="subscribe">SUBSCRIBE</div>
  <h3 style="left:618px">FOLLOW US</h3>
  <div class="socials" aria-label="Social media links"><span style="background:#3b5998"></span><span style="background:#2fa9e0"></span><span style="background:#1b75a8"></span><span style="background:#d6463a"></span></div>
</footer>
<div class="bottom-bar">© 2015.www.companyname.com. All rights reserved.</div>
</body>
</html>
```